Telepsychiatry Healthcare Services

I am a Family Medicine, Psychiatry Mental Health Nurse Practitioner, starting solo practice for mental health care for anxiety, depression, ptsd and adhd. Talk therapy with medication management if applicable. Would like to include my picture.

Target Market(s)

Children, Adolescent and Adults

Industry/Entity Type

Integrative Mental Healthcare

Requirements
Nice to have
• Mental Helath

```html
<!DOCTYPE html>
<html lang="en">
<head>
<meta charset="utf-8">
<title>MINDHAVEN Telepsychiatry Healthcare Services</title>
<link href="https://fonts.googleapis.com/css2?family=Playfair+Display:wght@600;700&family=Poppins:wght@400;500;600;700&display=swap" rel="stylesheet">
<style>
  :root {
    --navy: #161642;
    --navy-deep: #10102e;
    --purple: #5b2c8f;
    --plum: #6a1f5e;
    --green: #93d97c;
    --orange: #f0a04b;
    --red: #e2465a;
    --white: #ffffff;
    --photo: #d9dadf;
    --serif: "Playfair Display", Georgia, serif;
    --sans: "Poppins", Arial, sans-serif;
  }
  * { margin: 0; padding: 0; box-sizing: border-box; }
  html, body { width: 718px; height: 1200px; overflow: hidden; background: var(--navy); }
  .flyer {
    position: relative; width: 718px; height: 1200px; overflow: hidden;
    background: var(--navy); font-family: var(--sans); color: var(--white);
  }
  .brand {
    position: absolute; top: 126px; right: 42px;
    display: flex; align-items: center; gap: 14px;
  }
  .brand-dot { width: 26px; height: 26px; border-radius: 50%; background: var(--green); flex: none; }
  .brand-name {
    font-family: var(--sans); font-weight: 600; font-size: 19px; line-height: 1.35;
    letter-spacing: 2px; color: var(--green); text-transform: uppercase;
  }
  .hero-band {
    position: absolute; left: 0; top: 302px; width: 718px; height: 415px;
    background: linear-gradient(90deg, var(--purple) 0%, var(--plum) 100%);
  }
  .portrait { position: absolute; left: 0; top: 0; width: 420px; height: 740px; }
  .title-block { position: absolute; right: 35px; top: 330px; width: 300px; text-align: right; }
  .title {
    font-family: var(--serif); font-weight: 700; font-size: 39px; line-height: 56px; color: var(--white);
    white-space: nowrap;
  }
  .title-rule { height: 2px; background: var(--green); margin: 10px 0 12px 22px; }
  .services {
    font-family: var(--sans); font-weight: 600; font-size: 16px; line-height: 28px;
    color: var(--green); text-transform: uppercase; white-space: nowrap;
  }
  .feature { position: absolute; display: flex; align-items: center; gap: 14px; }
  .feature-left-top { left: 36px; top: 784px; }
  .feature-left-bottom { left: 36px; top: 912px; }
  .feature-right-top { left: 352px; top: 784px; }
  .feature-right-bottom { left: 352px; top: 912px; }
  .feature-icon { width: 82px; height: 82px; flex: none; }
  .feature-text { font-size: 11.3px; line-height: 16px; color: var(--white); white-space: nowrap; }
  .feature-text strong { color: var(--green); font-weight: 600; }
  .pricing {
    position: absolute; left: 35px; right: 35px; top: 1035px; height: 38px;
    background: var(--purple); border-radius: 16px 16px 0 0;
    font-size: 13px; font-weight: 600; line-height: 38px; text-align: center; color: var(--white);
    white-space: nowrap;
  }
  .pricing .fee { color: var(--orange); }
  .reassurance {
    position: absolute; left: 0; right: 0; top: 1073px; height: 45px;
    background: var(--orange); color: var(--navy-deep);
    font-family: var(--serif); font-weight: 600; font-size: 16px; line-height: 45px; text-align: center;
    white-space: nowrap;
  }
  .call-bar {
    position: absolute; left: 0; right: 0; top: 1118px; height: 82px; background: var(--navy-deep);
    display: flex; align-items: center; justify-content: center; gap: 32px;
  }
  .call-text { font-weight: 600; font-size: 20px; }
  .call-text .free { color: var(--green); }
  .phone { display: flex; align-items: center; gap: 10px; font-weight: 600; font-size: 26px; }
  .phone svg { width: 20px; height: 20px; }
</style>
</head>
<body>
<main class="flyer">

  <div class="brand">
    <span class="brand-dot"></span>
    <span class="brand-name">Mindhaven<br>Telepsychiatry</span>
  </div>

  <div class="hero-band"></div>

  <svg class="portrait" viewBox="0 0 420 740">
    <circle cx="150" cy="486" r="226" fill="var(--red)"/>
    <circle cx="158" cy="472" r="222" fill="var(--orange)"/>
    <circle cx="148" cy="458" r="214" fill="var(--photo)" role="img" aria-label="Portrait photograph of the nurse practitioner, smiling, in a dark top"/>
  </svg>

  <div class="title-block">
    <h1 class="title">MINDHAVEN<br>Telepsychiatry<br>Healthcare<br>Services</h1>
    <div class="title-rule"></div>
    <p class="services">Integrative mental health<br>services which includes:<br>anxiety, depression, PTSD,<br>ADHD, sleep disorders, etc.</p>
  </div>

  <div class="feature feature-left-top">
    <svg class="feature-icon" viewBox="0 0 80 80" fill="none" stroke="var(--green)" stroke-width="1.5">
      <circle cx="40" cy="40" r="38"/>
      <circle cx="40" cy="34" r="12"/>
      <circle cx="40" cy="34" r="6"/>
      <path d="M32 44 L27 60 L33 57 L36 62 L40 47 M48 44 L53 60 L47 57 L44 62 L40 47"/>
    </svg>
    <p class="feature-text"><strong>Expands over 25 years<br>in multiple Healthcare field</strong><br>and dually certified as a Family<br>Medicine &amp; Psychiatric Mental<br>Health Nurse Practitioner.</p>
  </div>

  <div class="feature feature-right-top">
    <svg class="feature-icon" viewBox="0 0 80 80" fill="none" stroke="var(--green)" stroke-width="1.5">
      <circle cx="40" cy="40" r="38"/>
      <path d="M18 58 L34 36 L42 46 L48 40 L62 58 Z"/>
      <path d="M40 38 V18 L52 22 L40 26"/>
    </svg>
    <p class="feature-text"><strong>Goal is to partner with individuals to<br>provide a safe place to explore life's<br>challenges, setbacks with motivational<br>timely expectations.</strong> These challenges<br>and setbacks can manifest itself in the<br>form of anxiety and depression.</p>
  </div>

  <div class="feature feature-left-bottom">
    <svg class="feature-icon" viewBox="0 0 80 80" fill="none" stroke="var(--green)" stroke-width="1.5">
      <circle cx="40" cy="40" r="38"/>
      <rect x="34" y="18" width="24" height="14" rx="2"/>
      <circle cx="30" cy="42" r="6"/>
      <path d="M19 60 V56 A11 11 0 0 1 41 56 V60 Z"/>
      <circle cx="50" cy="44" r="5"/>
      <path d="M41 60 V57 A9 9 0 0 1 59 57 V60"/>
    </svg>
    <p class="feature-text"><strong>Provide Talk Therapy online via<br>video which can assist with past<br>traumatic experiences</strong> with<br>medication management on an<br>as needed basis.</p>
  </div>

  <div class="feature feature-right-bottom">
    <svg class="feature-icon" viewBox="0 0 80 80" fill="none" stroke="var(--green)" stroke-width="1.5">
      <circle cx="40" cy="40" r="38"/>
      <path d="M28 20 V60 M40 20 V60 M52 20 V60"/>
      <rect x="24" y="26" width="8" height="8" rx="1" fill="var(--navy)"/>
      <rect x="36" y="44" width="8" height="8" rx="1" fill="var(--navy)"/>
      <rect x="48" y="32" width="8" height="8" rx="1" fill="var(--navy)"/>
    </svg>
    <p class="feature-text"><strong>Treatment plan will be customized</strong><br>on an individual basis.</p>
  </div>

  <div class="pricing">Carelink, Meridia, Healthwell, Private Pay, Sliding scale. Initial Eval <span class="fee">$275</span> (sliding scale $150-250)</div>

  <div class="reassurance">The struggle is real and you are not alone. We are here for you, because YOU matter.</div>

  <div class="call-bar">
    <p class="call-text">Call for a <span class="free">free consultation</span> now</p>
    <p class="phone">
      <svg viewBox="0 0 24 24" fill="var(--green)"><path d="M6.6 10.8a15.1 15.1 0 0 0 6.6 6.6l2.2-2.2a1 1 0 0 1 1-.25 11.4 11.4 0 0 0 3.6.57 1 1 0 0 1 1 1V20a1 1 0 0 1-1 1A17 17 0 0 1 3 4a1 1 0 0 1 1-1h3.5a1 1 0 0 1 1 1c0 1.25.2 2.45.57 3.57a1 1 0 0 1-.25 1z"/></svg>
      (555) 214-0837
    </p>
  </div>

</main>
</body>
</html>
```